R. Dunmore Homes, Inc business card (2 sided), letterhead (1 sided) & #10 envelope (1 sided)

business card of standard size utilizing the attached logo. Side one with logo, Carl Dunmore (my name), President / Broker (title), 805-555-0183 (phone), www.rdunmorehomes.example (website), 1275 Larkvale Avenue, Suite 4402 San Luis Obiso, CA 93499 (business address) carl.rdunmorehomes@mailbox.example (e-mail address),
Side two - Log

Letterhead and #10 envelope in the same theme

Reason: I think a 2 day deadline may be a bit ambitious on my part. I have extended the deadline to 4 days. Thanks!

```html
<!DOCTYPE html>
<html lang="en">
<head>
<meta charset="utf-8">
<title>R. Dunmore Homes, Inc – Business Card</title>
<link rel="stylesheet" href="https://fonts.googleapis.com/css2?family=Questrial&display=swap">
<style>
  :root {
    --brand-blue: #1f8fd1;
    --brand-blue-deep: #1774b4;
    --ink-grey: #5a5a5a;
    --soft-grey: #8a8a8a;
    --card-white: #ffffff;
    --page-bg: #e9e7e3;
    --rule-blue: #7ec1e8;
  }
  * { box-sizing: border-box; margin: 0; padding: 0; }
  html, body { width: 1200px; height: 1184px; overflow: hidden; }
  body {
    background: var(--page-bg);
    font-family: "Questrial", sans-serif;
    position: relative;
  }
  .card {
    position: absolute;
    left: 150px;
    width: 900px;
    height: 514px;
    border-radius: 4px;
    box-shadow: 0 6px 20px rgba(0,0,0,0.18);
    overflow: hidden;
  }
  /* Front: logo side */
  .card-front {
    top: 50px;
    background: linear-gradient(135deg, var(--brand-blue) 0%, var(--brand-blue-deep) 100%);
    color: var(--card-white);
    display: flex;
    flex-direction: column;
    align-items: center;
    justify-content: center;
  }
  .brand-name {
    display: flex;
    align-items: center;
    gap: 18px;
    font-size: 62px;
    letter-spacing: 1px;
    white-space: nowrap;
  }
  .brand-mark {
    width: 22px; height: 22px;
    background: currentColor;
  }
  .card-front .website {
    margin-top: 38px;
    font-size: 18px;
    letter-spacing: 6px;
  }
  /* Back: contact side */
  .card-back {
    top: 620px;
    background: var(--card-white);
    color: var(--ink-grey);
  }
  .card-back .brand-name {
    position: absolute;
    left: 60px; top: 54px;
    font-size: 34px;
    gap: 12px;
    color: var(--brand-blue-deep);
  }
  .card-back .brand-mark { width: 14px; height: 14px; }
  .person {
    position: absolute;
    left: 60px; top: 212px;
  }
  .person-name {
    font-size: 40px;
    line-height: 1.1;
    letter-spacing: 1px;
    text-transform: uppercase;
    color: var(--ink-grey);
    white-space: nowrap;
  }
  .person-name .first { color: var(--brand-blue); }
  .person-title {
    margin-top: 6px;
    font-size: 20px;
    letter-spacing: 11px;
    color: var(--soft-grey);
  }
  .divider {
    position: absolute;
    left: 400px; top: 252px;
    width: 440px; height: 1px;
    background: linear-gradient(90deg, rgba(126,193,232,0) 0%, var(--rule-blue) 35%, var(--rule-blue) 100%);
  }
  .address {
    position: absolute;
    right: 60px;
    text-align: right;
    font-size: 19px;
    line-height: 1;
    color: var(--ink-grey);
    white-space: nowrap;
  }
  .address-line1 {
    top: 216px;
    display: flex; align-items: center; justify-content: flex-end; gap: 8px;
  }
  .address-line2 { top: 266px; }
  .contacts {
    position: absolute;
    left: 110px; top: 380px;
    list-style: none;
    font-size: 21px;
    color: var(--soft-grey);
  }
  .contacts li { display: flex; align-items: center; gap: 14px; margin-bottom: 18px; }
  .contacts svg { flex: none; }
</style>
</head>
<body>

<section class="card card-front" aria-label="Business card, logo side">
  <div class="brand-name"><span class="brand-mark"></span>R. Dunmore Homes, Inc</div>
  <div class="website">www.rdunmorehomes.example</div>
</section>

<section class="card card-back" aria-label="Business card, contact side">
  <div class="brand-name"><span class="brand-mark"></span>R. Dunmore Homes, Inc</div>

  <div class="person">
    <div class="person-name"><span class="first">Carl</span>Dunmore</div>
    <div class="person-title">BROKER</div>
  </div>

  <div class="address address-line1">1275 Larkvale Avenue,
    <svg width="14" height="18" viewBox="0 0 14 18" aria-hidden="true">
      <path d="M7 0C3.1 0 0 3.1 0 7c0 5 7 11 7 11s7-6 7-11c0-3.9-3.1-7-7-7z" fill="#1f8fd1"/>
      <circle cx="7" cy="7" r="2.6" fill="#fff"/>
    </svg>
  </div>

  <div class="divider"></div>

  <div class="address address-line2">Suite 4402 San Luis Obiso, CA 93499</div>

  <ul class="contacts">
    <li>
      <svg width="16" height="24" viewBox="0 0 16 24" aria-hidden="true">
        <rect x="1" y="1" width="14" height="22" rx="2" fill="none" stroke="#1f8fd1" stroke-width="2"/>
        <rect x="4" y="4" width="8" height="12" fill="#1f8fd1"/>
        <circle cx="8" cy="19.5" r="1.3" fill="#1f8fd1"/>
      </svg>
      805-555-0183
    </li>
    <li>
      <svg width="18" height="13" viewBox="0 0 18 13" aria-hidden="true">
        <rect x="0" y="0" width="18" height="13" rx="1" fill="#1f8fd1"/>
        <path d="M1 1l8 6 8-6" fill="none" stroke="#fff" stroke-width="1.5"/>
      </svg>
      carl.rdunmorehomes@mailbox.example
    </li>
  </ul>
</section>

</body>
</html>
```